New Design for our Velintor Gran Reserva Brandy, it is the label design for the bottle label

We need a new bottle label for our Brandy Gran Reserva that we want to bring to the market.

Please have a look at all our current bottles and labels and the feel of our company under www.velintor-example.ch

The bottle that we will be using for the brand is a different one than the one that we already have, the design of the bottle is attached with a document.

I have also attached a briefing in regards to Brandy in general for your information.

### 1. What is Brandy?
Brandy is a distilled spirit made from fermented wine or other fruit wines. It is traditionally aged in oak barrels, which gives it its characteristic color and rich flavor. The aging process in oak is essential for developing the aromas and quality of the brandy.

### 2. What is Brandy Reserva?
A Brandy labeled as "Reserva" has undergone a longer aging process, typically at least 2 to 3 years, in oak barrels. This aging gives the brandy a deeper, more complex flavor profile and a darker color. "Reserva" is often an indication of higher quality.

### 3. Who enjoys drinking Brandy?
Brandy is typically favored by those who appreciate a deep, rich tasting experience. This often includes older consumers who value the time-aged complexity of the spirit. However, Brandy is also gaining popularity among younger people, especially through cocktails and modern serving styles.

### 4. Why is Brandy trending?
Brandy is experiencing a resurgence as consumers increasingly value quality and artisanal production methods. Its versatility in cocktails and association with traditional, luxurious experiences have also contributed to its renewed popularity.

### 5. What colors would be associated with Brandy?
The typical colors associated with Brandy are warm gold, amber, and deep golden-brown tones. These colors reflect the aging process in oak barrels and the richness of the flavors. Other associated colors might include dark brown and mahogany.

### 6. What is important to customers when buying Brandy?
Customers care about the origin of the Brandy, the aging time, the quality of the ingredients, the production method, and the brand. They also pay attention to the prestige of the product and the authenticity of the production.

### 7. What is not important to customers when buying Brandy?
For many customers, the price and packaging (unless it’s especially exclusive) may be less important than the quality and taste of the Brandy. The distillery name might be less significant if it isn’t tied to a particular reputation.

### 8. What do customers know about Swiss Brandy?
Swiss Brandy is still relatively unknown in many markets, but customers who are familiar with it appreciate the precision and quality of Swiss production. Swiss Brandy is assumed to be made with care and under strict quality standards.

### 9. What is Brandy Gran Reserva?
**Brandy Gran Reserva** is an even higher quality and longer-aged version of Brandy. Generally, a Gran Reserva is aged for at least 5 to 10 years or more in oak barrels. This extended aging process gives the Brandy an especially deep, complex flavor profile and often a darker, richer color. Gran Reserva is often regarded as the top-tier product within a Brandy range and appeals to discerning consumers who value quality, refinement, and a luxurious tasting experience.

The label “Gran Reserva” thus indicates the highest quality level for Brandies, similar to other spirits (like wine or whisky), where the aging time is a critical factor.

### 10. What emotions are associated with Brandy?
Brandy is often associated with luxury, relaxation, and comfort. It evokes feelings of tradition, elegance, and sophistication. Drinking Brandy is frequently seen as a moment of reflection and enjoyment.

### 11. How should Brandy be marketed?
Brandy should be marketed with a focus on its artisanal production, quality, and tradition. A narrative around the product, its aging, and origin can help create an emotional connection with the customer. The marketing should also emphasize the versatility of Brandy, whether consumed neat or in cocktails.

### 12. Sales test and label design for Velintor Brandy
For a sales test, I would suggest a tasting in an upscale setting, perhaps paired with a storytelling presentation highlighting the history of the 6-year aged Brandy and its aging in oak barrels.

**Label design**:
The label should reflect the exclusivity of the product, with an elegant, minimalist design. Colors like deep gold, mahogany, and a hint of deep blue could be used to emphasize the aging and quality of the Brandy. The label should include information about the aging time, the use of oak barrels, and a brief story about the Brandy’s production. A seal or embossing highlighting the craftsmanship would also be fitting.

Target Market(s)

Customers that like Brandy

Requirements
Must have
• the Alcohol % must be included on the label as well as our address.

```html
<!DOCTYPE html>
<html lang="en">
<head>
<meta charset="utf-8">
<title>Velintor Gran Reserva Brandy – Label</title>
<link href="https://fonts.googleapis.com/css2?family=Playfair+Display:ital,wght@0,400;0,600;0,900;1,400&family=Lato:wght@400;700&display=swap" rel="stylesheet">
<style>
  :root {
    --backdrop: #0c0b0c;
    --paper-light: #e4e2e0;
    --paper-mid: #b9b6b3;
    --paper-dark: #9e9a97;
    --frame-white: #f6f5f3;
    --frame-line: #8d8986;
    --mahogany: #4a1418;
    --brandy-red: #c8242c;
    --deep-blue: #1c2a8c;
    --gold: #c9a43a;
    --ink: #3a2a2a;
  }
  * { margin: 0; padding: 0; box-sizing: border-box; }
  html, body { width: 880px; height: 1200px; overflow: hidden; background: var(--backdrop); }
  .canvas {
    position: relative; width: 880px; height: 1200px;
    display: flex; align-items: center; justify-content: center;
  }
  .label {
    position: relative; width: 470px; height: 1120px;
    background: var(--frame-white);
    clip-path: polygon(34px 0, 436px 0, 470px 34px, 470px 100%, 0 100%, 0 34px);
  }
  .label-field {
    position: absolute; inset: 14px;
    background: radial-gradient(ellipse at 50% 45%, var(--paper-light) 0%, var(--paper-mid) 70%, var(--paper-dark) 100%);
    clip-path: polygon(26px 0, calc(100% - 26px) 0, 100% 26px, 100% 100%, 0 100%, 0 26px);
  }
  .label-frame { position: absolute; inset: 0; }
  .content {
    position: absolute; inset: 14px;
    display: flex; flex-direction: column; align-items: center;
    font-family: "Playfair Display", serif; color: var(--mahogany);
  }
  .house-row {
    margin-top: 92px; display: flex; align-items: center; gap: 14px;
    font-family: "Lato", sans-serif; font-size: 12px; letter-spacing: 3px; color: var(--gold);
  }
  .house-name {
    display: flex; align-items: center; gap: 8px;
    font-family: "Playfair Display", serif; font-size: 20px; font-weight: 600;
    letter-spacing: 1px; color: var(--mahogany);
  }
  .house-square { width: 10px; height: 10px; background: var(--brandy-red); }
  .brand-name {
    margin-top: 148px; font-size: 64px; font-weight: 400; letter-spacing: 1px;
    line-height: 1; color: var(--mahogany);
  }
  .spirit-type {
    margin-top: 6px; font-family: "Lato", sans-serif; font-size: 13px;
    letter-spacing: 6px; color: var(--ink);
  }
  .stars { margin-top: 116px; display: flex; align-items: center; gap: 18px; }
  .stars .rule { width: 26px; height: 1px; background: var(--gold); }
  .stars .diamond { width: 9px; height: 9px; background: var(--gold); transform: rotate(45deg); }
  .grade { margin-top: 90px; text-align: center; line-height: 0.95; }
  .grade-main { font-size: 76px; font-weight: 900; letter-spacing: 3px; color: var(--mahogany); }
  .grade-main .accent { color: var(--brandy-red); }
  .grade-sub { font-size: 36px; font-weight: 900; letter-spacing: 4px; color: var(--mahogany); }
  .age { margin-top: 66px; display: flex; align-items: flex-end; gap: 10px; }
  .age-word { font-family: "Lato", sans-serif; font-size: 12px; letter-spacing: 2px; color: var(--ink); padding-bottom: 14px; }
  .age-word em { font-family: "Playfair Display", serif; font-style: italic; letter-spacing: 0; }
  .age-number { font-size: 80px; font-weight: 400; line-height: 0.9; color: var(--deep-blue); }
  .story {
    margin-top: 40px; width: 380px; text-align: center;
    font-style: italic; font-size: 15px; line-height: 1.45; color: var(--ink);
  }
  .volume {
    margin-top: 30px; font-family: "Lato", sans-serif; font-size: 14px;
    letter-spacing: 2px; color: var(--ink);
  }
</style>
</head>
<body>
<main class="canvas">
  <section class="label">
    <div class="label-field"></div>
    <svg class="label-frame" width="470" height="1120" viewBox="0 0 470 1120" aria-hidden="true">
      <path d="M34 6 H436 L464 34 V1114 H6 V34 Z" fill="none" stroke="var(--frame-line)" stroke-width="1.5"/>
      <path d="M40 14 H430 L456 40 V1106 H14 V40 Z" fill="none" stroke="var(--frame-line)" stroke-width="1"/>
    </svg>
    <div class="content">
      <div class="house-row">
        <span>SINCE</span>
        <span class="house-name"><span class="house-square"></span>Velintor</span>
        <span>MMVI</span>
      </div>
      <h1 class="brand-name">VELINTOR</h1>
      <p class="spirit-type">BRANDY</p>
      <div class="stars">
        <span class="rule"></span>
        <span class="diamond"></span><span class="diamond"></span><span class="diamond"></span><span class="diamond"></span><span class="diamond"></span>
        <span class="rule"></span>
      </div>
      <div class="grade">
        <div class="grade-main">G<span class="accent">R</span>AN</div>
        <div class="grade-sub">RESERVA</div>
      </div>
      <div class="age">
        <span class="age-word">AGED <em>for</em></span>
        <span class="age-number">15</span>
        <span class="age-word">YEARS</span>
      </div>
      <p class="story">Distilled from Swiss wine and aged fifteen years in small oak casks, this brandy rests slowly until amber depth and warm spice emerge. Bottled by hand at Velintor, Rue du Chai 12, Vevey.</p>
      <p class="volume">500 ML · 40% VOL</p>
    </div>
  </section>
</main>
</body>
</html>
```